Business Card Design for Portrait photography professional

We are a small company specializing in portrait photography (weddings, family, couples, children, newborn, pregnant, etc.) Occasionally we do business portraits too and do some other type of photography. We need a business card which would fit into the same look and feel as our website theme (lumvira.com - under construction currently).
Our target customer base lies within mid- to upmarket. We want our business cards to convey a feeling of quality, solidness and a bit luxury.
Design should be universal and usable on 85mmx55mm, 90mmx50mm and 90mmx55mm
one extra file (PSD of a website didn't fit into the allowed updoad, therefore has put it into my dropbox: https://www.filqueso.com/s/qt8wr3kadhy5lbv/website%20theme%20PSD.psd)

Target Market(s)

mostly private people, 25-60 years old, mostly well established.

Industry/Entity Type

Portrait Photography

Requirements
Must have
• 2 sided design (print on both sides of the business card).
Must include:
business name, logo, URL (lumvira.no) , employee name, email address, and phone number.
Colorscheme of the website lumvira.no / lumvira.com

```html
<!DOCTYPE html>
<html lang="en">
<head>
<meta charset="utf-8">
<title>Lumvira Portraits – Business Card</title>
<link rel="stylesheet" href="https://fonts.googleapis.com/css2?family=Libre+Baskerville:wght@700&family=Comfortaa:wght@700&family=Questrial&display=swap">
<style>
  :root {
    --backdrop: #2b2a29;
    --cocoa: #3b3532;
    --cocoa-deep: #2f2a28;
    --linen: #c8c3b4;
    --linen-soft: #bdb7a7;
    --linen-text: #d2cdbf;
    --paper-edge: #eeebe3;
    --muted: #b3ada0;
  }
  * { box-sizing: border-box; margin: 0; padding: 0; }
  html, body { width: 1200px; height: 900px; overflow: hidden; }
  body { background: var(--backdrop); position: relative; }

  .card {
    position: absolute;
    width: 540px;
    height: 320px;
    border: 2px solid var(--paper-edge);
    overflow: hidden;
  }

  /* Front side */
  .card--front { left: 600px; top: 100px; background: var(--linen); }
  .card--front .pattern {
    position: absolute; inset: 0;
    background: radial-gradient(ellipse at 50% 50%, var(--linen) 0%, var(--linen-soft) 100%);
  }
  .card--front .band { position: absolute; left: 0; right: 0; height: 12px; background: var(--cocoa); }
  .card--front .band--top { top: 0; }
  .card--front .band--bottom { bottom: 0; }
  .front-mark {
    position: absolute; left: 50%; top: 62px; transform: translateX(-50%);
    width: 104px; height: 104px; border-radius: 50%;
    background: var(--cocoa-deep); border: 3px solid var(--paper-edge);
  }
  .front-name {
    position: absolute; left: 0; right: 0; top: 186px; text-align: center;
    font-family: "Libre Baskerville", serif; font-weight: 700;
    font-size: 27px; letter-spacing: 0.5px; color: var(--cocoa);
  }
  .front-url {
    position: absolute; left: 0; right: 0; top: 228px; text-align: center;
    font-family: "Questrial", sans-serif; font-size: 15px;
    letter-spacing: 9px; color: var(--cocoa);
  }

  /* Back side */
  .card--back { left: 140px; top: 470px; background: var(--cocoa); }
  .card--back .band { position: absolute; left: 0; right: 0; height: 18px; background: var(--linen); }
  .card--back .band--top { top: 0; }
  .card--back .band--bottom { bottom: 0; }
  .back-mark {
    position: absolute; left: 50%; top: 50px; transform: translateX(-50%);
    width: 58px; height: 58px; border-radius: 50%;
    border: 2px solid var(--linen-text);
  }
  .back-name {
    position: absolute; left: 0; right: 0; top: 128px; text-align: center;
    font-family: "Libre Baskerville", serif; font-weight: 700;
    font-size: 22px; letter-spacing: 0.3px; color: var(--linen-text);
  }
  .person {
    position: absolute; left: 40px; top: 226px;
    font-family: "Comfortaa", sans-serif; font-weight: 700;
    font-size: 16px; color: var(--linen-text);
  }
  .contacts {
    position: absolute; left: 40px; right: 30px; top: 206px; bottom: 24px;
    font-family: "Questrial", sans-serif; font-size: 13px; color: var(--muted);
  }
  .contact { position: absolute; display: flex; align-items: center; gap: 6px; }
  .contact--phone { right: 0; top: 0; }
  .contact--web { left: 180px; top: 22px; }
  .contact--mail { left: 0; top: 52px; }
  .contact-icon {
    width: 13px; height: 13px; background: var(--muted); color: var(--cocoa);
    font-size: 10px; line-height: 13px; text-align: center; font-family: "Questrial", sans-serif;
  }
  .contact-icon svg { display: block; }
</style>
</head>
<body>

  <section class="card card--front" aria-label="Card front">
    <div class="pattern" role="img" aria-label="Faint floral damask pattern in soft linen tones"></div>
    <div class="band band--top"></div>
    <div class="band band--bottom"></div>
    <div class="front-mark"></div>
    <h1 class="front-name">LUMVIRA PORTRAITS</h1>
    <p class="front-url">WWW.LUMVIRA.NO</p>
  </section>

  <section class="card card--back" aria-label="Card back">
    <div class="band band--top"></div>
    <div class="band band--bottom"></div>
    <div class="back-mark"></div>
    <h2 class="back-name">LUMVIRA PORTRAITS</h2>
    <p class="person">M.K. Halvorsen</p>
    <div class="contacts">
      <p class="contact contact--phone">
        <span class="contact-icon">
          <svg width="13" height="13" viewBox="0 0 13 13" aria-hidden="true">
            <rect x="4" y="1.5" width="5" height="10" rx="1" fill="#3b3532"/>
            <rect x="5" y="3" width="3" height="4" fill="#b3ada0"/>
          </svg>
        </span>
        : (+47) 412-60-358
      </p>
      <p class="contact contact--web"><span class="contact-icon">w</span>: www.lumvira.no</p>
      <p class="contact contact--mail"><span class="contact-icon">e</span>: info@lumvira.no</p>
    </div>
  </section>

</body>
</html>
```